New Business Card Design Project

Need a design that will create an impact / strong impression towards our clients for our business. We are in the lighting business and we do lighting retrofits for large commercial to industrial clientele.

Target Market(s)

Lighting Industry

Industry/Entity Type

Business

Font styles to use
Other font styles liked:
• we would like to use the font on our logo, not sure what it is though..

Requirements
Must have
• Our logo.
Nice to have
• We are open to suggestions that have to do with lighting.

```html
<!DOCTYPE html>
<html lang="en">
<head>
<meta charset="utf-8">
<title>Brightline Retrofit Co. – Business Cards</title>
<link href="https://fonts.googleapis.com/css2?family=Montserrat:wght@400;500;600&display=swap" rel="stylesheet">
<style>
  :root {
    --forest: #184315;
    --leaf: #5ccb4e;
    --ink: #3a3a3a;
    --paper: #ffffff;
    --backdrop: #e4e4e4;
  }
  html, body {
    margin: 0;
    padding: 0;
    width: 1200px;
    height: 800px;
    overflow: hidden;
  }
  body {
    background: radial-gradient(ellipse at 55% 45%, #f2f2f2 0%, var(--backdrop) 60%, #d6d6d6 100%);
    font-family: "Montserrat", sans-serif;
    position: relative;
  }
  .card {
    position: absolute;
    top: 250px;
    width: 520px;
    height: 290px;
    box-sizing: border-box;
    box-shadow: 0 10px 24px rgba(0,0,0,0.18);
  }
  .card-front {
    left: 50px;
    background: var(--paper);
    padding: 34px 34px 30px 0;
  }
  .card-back {
    left: 630px;
    background: var(--forest);
    display: flex;
    align-items: center;
    justify-content: center;
  }
  .brand {
    display: flex;
    align-items: center;
    gap: 10px;
    font-weight: 600;
    letter-spacing: 0.04em;
    text-transform: uppercase;
  }
  .brand-mark {
    width: 14px;
    height: 14px;
  }
  .card-front .brand {
    position: absolute;
    top: 40px;
    right: 36px;
    font-size: 20px;
    color: var(--forest);
  }
  .card-front .brand-mark { background: var(--leaf); }
  .card-back .brand {
    font-size: 28px;
    color: var(--paper);
  }
  .card-back .brand-mark { background: var(--paper); width: 18px; height: 18px; }
  .holder {
    position: absolute;
    left: 0;
    top: 170px;
    padding-left: 28px;
    border-left: 5px solid var(--leaf);
  }
  .holder-name {
    margin: 0;
    font-size: 20px;
    font-weight: 600;
    color: var(--forest);
    letter-spacing: 0.02em;
    line-height: 1.1;
  }
  .holder-title {
    margin: 2px 0 0;
    font-size: 13px;
    color: var(--ink);
  }
  .contact {
    position: absolute;
    left: 33px;
    top: 232px;
    font-size: 13px;
    color: var(--ink);
  }
  .contact-row {
    display: flex;
    align-items: center;
  }
  .contact-row span + span {
    border-left: 3px solid var(--leaf);
    margin-left: 14px;
    padding-left: 14px;
  }
  .contact-address {
    margin-top: 14px;
  }
</style>
</head>
<body>
  <section class="card card-front" aria-label="Business card front">
    <div class="brand">
      <span class="brand-name">Brightline Retrofit Co.</span>
      <span class="brand-mark"></span>
    </div>
    <div class="holder">
      <h1 class="holder-name">OWEN HARTLEY</h1>
      <p class="holder-title">Director Executive</p>
    </div>
    <div class="contact">
      <div class="contact-row">
        <span>(555) 014-2270</span>
        <span>hello@brightline-co.com</span>
        <span>www.brightline-co.com</span>
      </div>
      <div class="contact-address">1480 Linden Avenue Marlow, IL 60900</div>
    </div>
  </section>

  <section class="card card-back" aria-label="Business card back">
    <div class="brand">
      <span class="brand-name">Brightline Retrofit Co.</span>
      <span class="brand-mark"></span>
    </div>
  </section>
</body>
</html>
```